Stationery and business cards for new pediatric urgent care
Little Sprouts Urgent Care
Stationery and business cards for new pediatric urgent care  - Medical
Creative Brief
Bright & Fun-filled
Myles T. Rowan MD, Pediatrics
2718 North 41st West Cedar Bend, NV 83511
myles.rowan@littlesproutsurgentcare-example.com
www.littlesproutsurgentcare-example.com

```html
<!DOCTYPE html>
<html lang="en">
<head>
<meta charset="utf-8">
<title>Little Sprouts Urgent Care – Stationery Concepts</title>
<link rel="stylesheet" href="https://fonts.googleapis.com/css2?family=Montserrat:wght@400;700;800&family=Open+Sans:wght@400;600&family=Great+Vibes&display=swap">
<style>
:root{
  --bg:#353535;
  --blue:#1b86b4;
  --orange:#ef7f22;
  --paper:#ffffff;
  --ink:#555555;
  --rule:#d9d9d9;
  --soft:#f2f2f2;
}
*{box-sizing:border-box;margin:0;padding:0}
html,body{width:1200px;height:254px;overflow:hidden;background:var(--bg)}
body{position:relative;font-family:"Open Sans",sans-serif;color:var(--ink)}
.piece{position:absolute;background:var(--paper);overflow:hidden}
.piece.blue{background:var(--blue)}
.piece::after{content:"";position:absolute;left:0;right:0;bottom:0;height:2px;background:linear-gradient(90deg,var(--blue) 78%,var(--orange) 78%)}
.piece.noedge::after{display:none}
.brand{font-family:"Montserrat",sans-serif;font-weight:800;color:var(--blue);line-height:1;white-space:nowrap}
.brand span{display:block;font-size:.5em;letter-spacing:.18em;margin-top:1px}
.on-blue .brand,.brand.white{color:var(--paper)}
.tiny{font-size:2.6px;line-height:1.35;color:var(--ink);overflow-wrap:anywhere}
.intro{position:absolute;left:14px;top:34px;width:92px;text-align:center;color:var(--paper)}
.intro .brand{color:var(--paper);font-size:7px}
.intro p{font-family:"Montserrat",sans-serif;font-size:4.4px;margin-top:2px}
.script{font-family:"Great Vibes",cursive;color:var(--blue)}
.sig{position:absolute;width:22px;height:6px;background:linear-gradient(90deg,#c9d9e3,#e6eef3)}
.circle{position:absolute;border-radius:50%;display:flex;align-items:center;justify-content:center;flex-direction:column}
.hole{width:20%;height:20%;border-radius:50%;background:var(--paper);border:1.5px solid #222}
.slide h3{font-family:"Montserrat",sans-serif;font-size:4.5px;color:var(--blue);font-weight:700}
.slide h4{font-size:2.5px;color:var(--orange);font-weight:600}
.slide .head{position:absolute;left:6px;top:5px;right:6px;border-bottom:.5px solid var(--rule);padding-bottom:2px}
.dot{position:absolute;right:6px;top:6px;width:5px;height:5px;background:var(--blue);border-radius:50%}
</style>
</head>
<body>

<!-- Intro -->
<div class="intro">
  <div class="brand">Little Sprouts<span>URGENT CARE</span></div>
  <p>Stationery Concepts</p>
</div>

<!-- Business cards -->
<div class="piece blue on-blue noedge" style="left:7px;top:57px;width:46px;height:27px">
  <div class="brand" style="position:absolute;left:6px;top:8px;font-size:5px">Little Sprouts<span>URGENT CARE</span></div>
</div>
<div class="piece" style="left:57px;top:57px;width:46px;height:27px">
  <div class="brand" style="position:absolute;left:3px;top:9px;font-size:3.4px">Little Sprouts<span>URGENT CARE</span></div>
  <div class="tiny" style="position:absolute;left:25px;top:6px;width:19px;font-size:1.6px"><b>Myles T. Rowan</b><br>MD, Pediatrics<br>(208) 555-0147<br>2718 North 41st West<br>Cedar Bend, NV 83511</div>
</div>
<div class="piece" style="left:7px;top:91px;width:46px;height:27px">
  <div class="brand" style="position:absolute;left:6px;top:9px;font-size:5px">Little Sprouts<span>URGENT CARE</span></div>
</div>
<div class="piece" style="left:57px;top:91px;width:46px;height:27px">
  <div class="brand" style="position:absolute;left:3px;top:4px;font-size:4.2px">Little Sprouts<span>URGENT CARE</span></div>
  <div class="tiny" style="position:absolute;left:3px;top:14px;width:17px;font-size:1.6px"><b>Myles T. Rowan</b><br>MD, Pediatrics</div>
  <div class="tiny" style="position:absolute;left:22px;top:14px;width:22px;font-size:1.6px">(208) 555-0147<br>Cedar Bend, NV 83511</div>
</div>

<!-- Letterheads -->
<div class="piece" style="left:109px;top:15px;width:81px;height:101px">
  <div class="brand" style="position:absolute;left:6px;top:7px;font-size:4px">Little Sprouts<span>URGENT CARE</span></div>
  <div class="tiny" style="position:absolute;left:50px;top:5px;width:28px;font-size:1.6px">2718 North 41st West<br>Cedar Bend, NV 83511<br>(208) 555-0147<br>myles.rowan@littlesprouts urgentcare-example.com</div>
  <div class="tiny" style="position:absolute;left:6px;top:24px;font-size:1.6px">Date<br><br><b>Recipient Name</b><br>Company Name<br>Street Address<br>City, State, Zip</div>
  <div class="tiny" style="position:absolute;left:6px;top:42px;width:68px;font-size:1.6px">Thank you for trusting our team with the care of your child. Our clinic is open every day with short waits and friendly staff who love kids. We look forward to seeing your family soon and keeping everyone healthy, happy and growing strong all year long.</div>
  <div class="sig" role="img" aria-label="Handwritten signature" style="left:6px;top:80px"></div>
  <div class="tiny" style="position:absolute;left:6px;top:88px;font-size:1.6px"><b>Myles T. Rowan</b><br>MD, Pediatrics</div>
</div>
<div class="piece" style="left:193px;top:15px;width:77px;height:101px">
  <div class="brand" style="position:absolute;left:27px;top:7px;font-size:4px">Little Sprouts<span>URGENT CARE</span></div>
  <div class="tiny" style="position:absolute;left:6px;top:24px;font-size:1.6px">Date<br><br><b>Recipient Name</b><br>Company Name<br>City, State, Zip</div>
  <div class="tiny" style="position:absolute;left:6px;top:40px;width:65px;font-size:1.6px">Thank you for trusting our team with the care of your child. Our clinic is open every day with short waits and friendly staff who love kids. We look forward to seeing your family.</div>
  <div class="sig" role="img" aria-label="Handwritten signature" style="left:6px;top:80px"></div>
  <div class="tiny" style="position:absolute;left:4px;right:4px;bottom:4px;text-align:center;font-size:1.5px">2718 North 41st West, Cedar Bend, NV 83511 · www.littlesproutsurgentcare-example.com</div>
</div>

<!-- Pen and pencil bars -->
<div class="piece blue noedge" style="left:284px;top:17px;width:76px;height:3px;border-radius:2px"></div>
<div class="piece noedge" style="left:284px;top:31px;width:76px;height:2px;background:#222;border-radius:1px"></div>

<!-- Email signature card -->
<div class="piece" style="left:293px;top:42px;width:61px;height:28px">
  <div class="brand" style="position:absolute;left:12px;top:4px;font-size:4.4px">Little Sprouts<span>URGENT CARE</span></div>
  <div class="tiny" style="position:absolute;left:8px;top:15px;width:20px;font-size:1.6px"><b>Myles T. Rowan</b><br>MD, Pediatrics</div>
  <div class="tiny" style="position:absolute;left:31px;top:15px;width:26px;font-size:1.6px">(208) 555-0147<br>Cedar Bend, NV 83511</div>
</div>

<!-- Envelope front -->
<div class="piece" style="left:276px;top:80px;width:84px;height:36px">
  <div class="brand" style="position:absolute;left:4px;top:4px;font-size:3.6px">Little Sprouts<span>URGENT CARE</span></div>
</div>

<!-- Envelope backs -->
<div class="piece blue noedge" style="left:376px;top:40px;width:84px;height:14px">
  <div class="tiny" style="position:absolute;left:0;right:0;bottom:2px;text-align:center;color:#fff;font-size:1.5px">www.littlesproutsurgentcare-example.com</div>
</div>
<div class="piece noedge" style="left:370px;top:60px;width:80px;height:14px;background:var(--orange)"></div>
<div class="piece" style="left:364px;top:80px;width:84px;height:36px">
  <svg width="84" height="36" style="position:absolute;left:0;top:0"><path d="M0 0 L42 20 L84 0" fill="none" stroke="#dddddd" stroke-width=".6"/></svg>
</div>

<!-- Folder -->
<div class="piece blue noedge" style="left:466px;top:18px;width:57px;height:100px;border-left:3px solid var(--orange)">
  <div class="tiny" style="position:absolute;left:3px;bottom:8px;color:#fff;font-size:1.5px">2718 North 41st West<br>Cedar Bend, NV 83511</div>
</div>
<div class="piece" style="left:523px;top:18px;width:57px;height:100px;border-right:3px solid var(--orange)">
  <div class="brand" style="position:absolute;left:17px;top:33px;font-size:5px">Little Sprouts<span>URGENT CARE</span></div>
</div>

<!-- Fax sheets -->
<div class="piece" style="left:595px;top:16px;width:77px;height:101px">
  <div class="brand" style="position:absolute;left:5px;top:5px;font-size:3.6px">Little Sprouts<span>URGENT CARE</span></div>
  <svg width="68" height="16" style="position:absolute;left:5px;top:18px">
    <g fill="#ececec"><rect x="12" y="0" width="20" height="3"/><rect x="46" y="0" width="20" height="3"/><rect x="12" y="4" width="20" height="3"/><rect x="46" y="4" width="20" height="3"/><rect x="12" y="8" width="20" height="3"/><rect x="46" y="8" width="20" height="3"/><rect x="12" y="12" width="20" height="3"/><rect x="46" y="12" width="20" height="3"/></g>
  </svg>
  <div class="tiny" style="position:absolute;left:5px;top:18px;font-size:1.6px;line-height:2.5">To<br>Fax<br>Phone<br>Re</div>
  <div class="tiny" style="position:absolute;left:5px;top:37px;font-size:1.6px">Urgent · For Review · Please Reply<br><br>Comments:</div>
</div>
<div class="piece" style="left:678px;top:16px;width:77px;height:101px">
  <div class="brand" style="position:absolute;left:27px;top:5px;font-size:3.6px">Little Sprouts<span>URGENT CARE</span></div>
  <svg width="68" height="16" style="position:absolute;left:5px;top:18px">
    <g fill="#ececec"><rect x="12" y="0" width="20" height="3"/><rect x="46" y="0" width="20" height="3"/><rect x="12" y="4" width="20" height="3"/><rect x="46" y="4" width="20" height="3"/><rect x="12" y="8" width="20" height="3"/><rect x="46" y="8" width="20" height="3"/><rect x="12" y="12" width="20" height="3"/><rect x="46" y="12" width="20" height="3"/></g>
  </svg>
  <div class="tiny" style="position:absolute;left:5px;top:18px;font-size:1.6px;line-height:2.5">To<br>Fax<br>Phone<br>Re</div>
  <div class="tiny" style="position:absolute;left:5px;top:37px;font-size:1.6px">Urgent · For Review · Please Reply<br><br>Comments:</div>
</div>

<!-- Compliment slip -->
<div class="piece" style="left:770px;top:27px;width:86px;height:36px">
  <div class="brand" style="position:absolute;left:5px;top:5px;font-size:3.6px">Little Sprouts<span>URGENT CARE</span></div>
  <div class="script" style="position:absolute;left:5px;top:19px;font-size:9px">With Compliments</div>
</div>

<!-- Thank you cards -->
<div class="piece" style="left:763px;top:73px;width:48px;height:35px">
  <div class="brand" style="position:absolute;left:6px;top:5px;font-size:3.6px">Little Sprouts<span>URGENT CARE</span></div>
  <div class="script" style="position:absolute;left:6px;top:17px;font-size:9px">Thank you</div>
</div>
<div class="piece blue on-blue noedge" style="left:818px;top:73px;width:48px;height:35px">
  <div class="circle" style="left:16px;top:6px;width:16px;height:16px;background:#fff"></div>
  <div class="tiny" style="position:absolute;left:0;right:0;top:26px;text-align:center;color:#fff;font-size:1.5px">2718 North 41st West<br>Cedar Bend, NV 83511</div>
</div>

<!-- CD and cover (top) -->
<div class="circle" style="left:871px;top:7px;width:58px;height:58px;background:var(--blue)">
  <div class="brand white" style="font-size:3.6px;text-align:center;margin-bottom:3px">Little Sprouts<span>URGENT CARE</span></div>
  <div class="hole" style="width:13px;height:13px"></div>
</div>
<div class="piece" style="left:935px;top:12px;width:60px;height:48px">
  <div class="piece blue noedge" style="left:0;top:0;width:60px;height:8px"></div>
  <div class="brand" style="position:absolute;left:4px;top:12px;font-size:3.4px">Little Sprouts<span>URGENT CARE</span></div>
</div>

<!-- Screens -->
<div class="piece blue on-blue noedge" style="left:873px;top:72px;width:56px;height:40px;border:2px solid #111">
  <div class="brand" style="position:absolute;left:9px;top:14px;font-size:4.6px">Little Sprouts<span>URGENT CARE</span></div>
</div>
<div class="piece blue on-blue noedge" style="left:940px;top:74px;width:19px;height:36px;border:1.5px solid #eee;border-radius:2px">
  <div class="brand" style="position:absolute;left:2px;top:15px;font-size:2.2px">Little Sprouts<span>URGENT CARE</span></div>
</div>
<div class="piece noedge" style="left:966px;top:74px;width:19px;height:36px;background:#111;border-radius:2px">
  <div class="brand white" style="position:absolute;left:2px;top:15px;font-size:2.2px">Little Sprouts<span>URGENT CARE</span></div>
</div>

<!-- Presentation slides -->
<div class="piece slide" style="left:1001px;top:13px;width:92px;height:69px">
  <div class="brand" style="position:absolute;left:8px;top:10px;font-size:7.5px">Little Sprouts<span>URGENT CARE</span></div>
  <h3 style="position:absolute;left:8px;top:44px;color:var(--orange);font-size:3.8px;line-height:1.2">WELCOME TO OUR<br>PRESENTATION NAME<br>DESCRIPTION</h3>
</div>
<div class="piece slide" style="left:1100px;top:13px;width:91px;height:69px">
  <div class="head"><h3>Heading Here</h3><h4>Sub Heading</h4></div>
  <div class="dot"></div>
  <div role="img" aria-label="Team member photo" style="position:absolute;left:6px;top:20px;width:17px;height:17px;background:#8a8a8a"></div>
  <div role="img" aria-label="Team member photo" style="position:absolute;left:26px;top:20px;width:17px;height:17px;background:#8a8a8a"></div>
  <div role="img" aria-label="Team member photo" style="position:absolute;left:47px;top:20px;width:17px;height:17px;background:#8a8a8a"></div>
  <div role="img" aria-label="Team member photo" style="position:absolute;left:68px;top:20px;width:17px;height:17px;background:#8a8a8a"></div>
  <div class="tiny" style="position:absolute;left:6px;top:41px;width:80px;font-size:1.6px;color:var(--blue)">Team member1 &nbsp; Team member2 &nbsp; Team member3 &nbsp; Team member4</div>
</div>
<div class="piece slide" style="left:1001px;top:89px;width:92px;height:69px">
  <div class="head"><h3>Heading Here</h3><h4>Sub Heading</h4></div>
  <div class="dot"></div>
  <div class="tiny" style="position:absolute;left:6px;top:18px;width:38px;font-size:1.5px"><b style="color:var(--blue)">Group1</b><br>Short notes on services and visit hours.<br><br><b style="color:var(--blue)">Group2</b><br>Short notes on care team and staff.<br><br><b style="color:var(--blue)">Group3</b><br>Short notes on insurance and billing.</div>
  <div class="tiny" style="position:absolute;left:48px;top:18px;width:38px;font-size:1.5px"><b style="color:var(--blue)">Group4</b><br>Short notes on family resources.<br><br><b style="color:var(--blue)">Group5</b><br>Short notes on walk-in visits.<br><br><b style="color:var(--blue)">Group6</b><br>Short notes on follow-up care.</div>
</div>
<div class="piece slide" style="left:1100px;top:89px;width:91px;height:69px">
  <div class="head"><h3>Heading Here</h3><h4>Sub Heading</h4></div>
  <div class="dot"></div>
  <svg width="40" height="32" style="position:absolute;left:8px;top:18px">
    <g fill="var(--blue)"><rect x="2" y="6" width="5" height="26"/><rect x="9" y="10" width="5" height="22"/><rect x="16" y="14" width="5" height="18"/><rect x="23" y="12" width="5" height="20"/><rect x="30" y="16" width="5" height="16"/></g>
    <path d="M0 32H40" stroke="#999" stroke-width=".4"/>
  </svg>
  <div class="tiny" style="position:absolute;left:52px;top:20px;width:34px;font-size:1.5px">Visits grew each month this year as more families chose our clinic.</div>
</div>
<div class="piece slide" style="left:1001px;top:165px;width:92px;height:69px">
  <div class="head"><h3>Heading Here</h3><h4>Sub Heading</h4></div>
  <div class="dot"></div>
  <div class="tiny" style="position:absolute;left:6px;top:18px;width:48px;font-size:1.5px">Our care team sees children of every age with short waits, clear answers and gentle hands. Parents trust us for fevers, cuts, sprains and sudden sick days.</div>
  <svg width="24" height="24" viewBox="-12 -12 24 24" style="position:absolute;left:60px;top:20px">
    <circle r="10" fill="var(--blue)"/>
    <path d="M0 0 L0 -10 A10 10 0 0 1 9.5 3.1 Z" fill="var(--orange)"/>
  </svg>
</div>
<div class="piece blue slide noedge" style="left:1100px;top:165px;width:91px;height:69px">
  <div style="position:absolute;left:8px;top:10px;font-family:'Montserrat',sans-serif;color:#fff;font-size:13px;line-height:1">Thanks</div>
  <div style="position:absolute;left:8px;top:24px;font-family:'Montserrat',sans-serif;color:#fff;font-size:7px">For Coming</div>
  <div class="tiny" style="position:absolute;left:8px;top:52px;color:#fff;font-size:1.5px">2718 North 41st West<br>Cedar Bend, NV 83511<br>(208) 555-0147</div>
</div>

<!-- Bottom row: folder inside -->
<div class="piece" style="left:14px;top:140px;width:180px;height:80px;border-left:3px solid var(--orange);border-right:3px solid var(--orange)">
  <div class="piece blue noedge" style="left:8px;top:44px;width:70px;height:36px"></div>
  <div class="piece blue noedge" style="left:96px;top:44px;width:70px;height:36px"></div>
  <div style="position:absolute;left:86px;top:0;bottom:0;width:.5px;background:var(--rule)"></div>
</div>

<!-- Stickers -->
<div class="circle" style="left:212px;top:160px;width:40px;height:40px;background:#fff;border:2px solid var(--orange)">
  <div class="brand" style="font-size:2.6px;text-align:center">Little Sprouts<span>URGENT CARE</span></div>
</div>
<div class="circle" style="left:258px;top:160px;width:40px;height:40px;background:var(--blue)">
  <div class="circle" style="position:static;width:14px;height:14px;background:#fff"></div>
</div>
<div class="circle" style="left:304px;top:160px;width:40px;height:40px;background:var(--orange)">
  <div class="circle" style="position:static;width:14px;height:14px;background:#fff"></div>
</div>
<div class="circle" style="left:350px;top:160px;width:40px;height:40px;background:#fff;border:2px solid var(--blue)">
  <div class="brand" style="font-size:2.6px;text-align:center">Little Sprouts<span>URGENT CARE</span></div>
</div>

<!-- CD labels -->
<div class="circle" style="left:405px;top:135px;width:55px;height:55px;background:var(--blue)">
  <div class="brand white" style="font-size:3.2px;text-align:center;margin-bottom:3px">Little Sprouts<span>URGENT CARE</span></div>
  <div class="hole" style="width:12px;height:12px"></div>
</div>
<div class="circle" style="left:470px;top:135px;width:55px;height:55px;background:var(--orange)">
  <div class="brand white" style="font-size:3.2px;text-align:center;margin-bottom:3px">Little Sprouts<span>URGENT CARE</span></div>
  <div class="hole" style="width:12px;height:12px"></div>
</div>
<div class="circle" style="left:405px;top:195px;width:55px;height:55px;background:#fff;border:2px solid var(--blue)">
  <div class="brand" style="font-size:3.2px;text-align:center;margin-bottom:3px">Little Sprouts<span>URGENT CARE</span></div>
  <div class="hole" style="width:12px;height:12px"></div>
</div>
<div class="circle" style="left:470px;top:195px;width:55px;height:55px;background:var(--blue)">
  <div class="circle" style="position:absolute;left:6px;top:6px;width:43px;height:43px;background:#fff"></div>
  <div class="brand" style="font-size:3.2px;text-align:center;margin-bottom:3px;position:relative">Little Sprouts<span>URGENT CARE</span></div>
  <div class="hole" style="width:12px;height:12px;position:relative"></div>
</div>

<!-- CD covers -->
<div class="piece blue on-blue noedge" style="left:545px;top:140px;width:58px;height:42px">
  <div class="brand" style="position:absolute;left:5px;top:5px;font-size:3.2px">Little Sprouts<span>URGENT CARE</span></div>
  <div class="tiny" style="position:absolute;left:5px;bottom:5px;color:#fff;font-size:1.5px">2718 North 41st West, Cedar Bend, NV 83511</div>
</div>
<div class="piece" style="left:545px;top:192px;width:58px;height:42px">
  <div class="brand" style="position:absolute;left:5px;top:5px;font-size:3.2px">Little Sprouts<span>URGENT CARE</span></div>
  <div class="tiny" style="position:absolute;left:5px;bottom:5px;font-size:1.5px">2718 North 41st West, Cedar Bend, NV 83511</div>
</div>

<!-- Screen splashes -->
<div class="piece noedge" style="left:620px;top:142px;width:58px;height:40px;background:#fff;border:2px solid #111">
  <div class="brand" style="position:absolute;left:10px;top:14px;font-size:4.4px">Little Sprouts<span>URGENT CARE</span></div>
</div>
<div class="piece noedge" style="left:620px;top:194px;width:58px;height:40px;background:#000;border:2px solid #222">
  <div class="brand" style="position:absolute;left:10px;top:14px;font-size:4.4px">Little Sprouts<span>URGENT CARE</span></div>
</div>
<div class="piece noedge" style="left:690px;top:142px;width:20px;height:40px;background:#fff;border:1.5px solid #ddd;border-radius:2px">
  <div class="brand" style="position:absolute;left:2px;top:16px;font-size:2.2px">Little Sprouts<span>URGENT CARE</span></div>
</div>
<div class="piece noedge" style="left:690px;top:194px;width:20px;height:40px;background:#fff;border:1.5px solid #ddd;border-radius:2px">
  <div class="brand" style="position:absolute;left:2px;top:16px;font-size:2.2px">Little Sprouts<span>URGENT CARE</span></div>
</div>

</body>
</html>
```